Harbor Lantern Business Card
remarkable business card
Project: Harbor Lantern Business Card
Harbor Lantern Business Card - Events
Creative Brief
Use specific fonts
Use the fonts in my logo and/or the fonts that look best
Bright & Fun-filled
Tom Vesk
Culture Director
not to be listed on the card
Vesk@HarborLantern.example
www.HarborLantern.example
I want the Name to be prominent . I don't want the address to be listed This should be a very remarkable card. It needs to get instant attention that people will remember, and talk about. People should say wow! you need to see this card. That is a great looking card!

```html
<!DOCTYPE html>
<html lang="en">
<head>
<meta charset="utf-8">
<title>Harbor Lantern Business Card</title>
<link rel="stylesheet" href="https://fonts.googleapis.com/css2?family=EB+Garamond:ital,wght@0,400;0,600;1,400&display=swap">
<style>
  :root {
    --backdrop: #e9e6e1;
    --card: #ffffff;
    --ink: #3a3a3a;
    --green: #6ea528;
    --green-light: #8cc63f;
    --blue: #1d5fb0;
    --blue-deep: #13448a;
    --rule: #b9b9b9;
  }
  * { margin: 0; padding: 0; box-sizing: border-box; }
  html, body {
    width: 1200px; height: 780px; overflow: hidden;
    background: var(--backdrop);
    font-family: "EB Garamond", Georgia, serif;
    color: var(--ink);
  }
  .card {
    position: absolute; left: 100px; top: 105px;
    width: 1000px; height: 570px;
    background: var(--card);
    border-radius: 30px;
    overflow: hidden;
    box-shadow: 0 10px 30px rgba(0,0,0,.18);
  }
  .brand {
    position: absolute; left: 90px; top: 95px;
    display: flex; align-items: center; gap: 26px;
  }
  .brand-dot {
    width: 110px; height: 110px; border-radius: 50%;
    background: var(--green-light);
    flex: none;
  }
  .brand-text {
    display: flex; flex-direction: column; align-items: flex-end;
  }
  .brand-name {
    font-size: 72px; font-weight: 600; color: var(--green);
    line-height: 1; letter-spacing: -0.5px;
  }
  .tagline {
    margin-top: 4px;
    font-size: 27px; font-style: italic; color: var(--green);
    line-height: 1.1;
  }
  .person {
    position: absolute; right: 560px; top: 298px;
    text-align: right;
  }
  .person-name {
    font-size: 36px; font-weight: 600; color: var(--green); line-height: 1.1;
  }
  .person-title { font-size: 25px; color: var(--ink); }
  .divider {
    position: absolute; left: 468px; top: 275px;
    width: 2px; height: 135px; background: var(--rule);
  }
  .contacts {
    position: absolute; left: 492px; top: 278px;
    list-style: none; font-size: 25px; line-height: 42px;
  }
  .contacts li { display: flex; align-items: center; gap: 14px; }
  .contacts svg { width: 22px; height: 22px; fill: var(--green); flex: none; }
  .footer-band { position: absolute; left: 0; bottom: 0; width: 1000px; height: 200px; }
  .website {
    position: absolute; left: 0; right: 0; bottom: 24px;
    text-align: center; font-size: 24px; color: #ffffff; letter-spacing: .3px;
  }
</style>
</head>
<body>
  <div class="card">
    <div class="brand">
      <span class="brand-dot"></span>
      <div class="brand-text">
        <span class="brand-name">Harbor Lantern</span>
        <p class="tagline">Lighting the way for every home</p>
      </div>
    </div>

    <div class="person">
      <p class="person-name">Tom Vesk</p>
      <p class="person-title">Culture Director</p>
    </div>
    <span class="divider"></span>
    <ul class="contacts">
      <li>
        <svg viewBox="0 0 24 24" aria-hidden="true"><rect x="6" y="1" width="12" height="22" rx="2"/><rect x="8" y="4" width="8" height="12" fill="#fff"/></svg>
        555-014-2273
      </li>
      <li>
        <svg viewBox="0 0 24 24" aria-hidden="true"><path d="M3 9c0-3 4-5 9-5s9 2 9 5v2h-5V8H8v3H3z"/><rect x="5" y="12" width="14" height="9" rx="1.5"/></svg>
        555-018-6604
      </li>
      <li>
        <svg viewBox="0 0 24 24" aria-hidden="true"><rect x="1" y="5" width="22" height="14" rx="1.5"/><path d="M2 6l10 7 10-7" fill="none" stroke="#fff" stroke-width="2"/></svg>
        Vesk@HarborLantern.example
      </li>
    </ul>

    <svg class="footer-band" viewBox="0 0 1000 200" preserveAspectRatio="none" aria-hidden="true">
      <defs>
        <linearGradient id="bandBlue" x1="0" y1="0" x2="1" y2="0">
          <stop offset="0" stop-color="#13448a"/>
          <stop offset="0.5" stop-color="#1d5fb0"/>
          <stop offset="1" stop-color="#13448a"/>
        </linearGradient>
      </defs>
      <path d="M0 95 C 300 150, 650 110, 1000 10 L1000 40 C 650 135, 300 170, 0 120 Z" fill="#8cc63f"/>
      <path d="M0 118 C 300 168, 650 135, 1000 35 L1000 200 L0 200 Z" fill="url(#bandBlue)"/>
    </svg>
    <p class="website">www.HarborLantern.example</p>
  </div>
</body>
</html>
```